Mr Glimmo Car Wash Menu Brochure

Front/Back brochure with Car Wash Menu Options & pricing
(size : 8.5" x 3.66" - front/back)

Side 1:
Logo on top
"Wash Menu"
- Ultimate Glimmo - $19
- includes Brisk & Bloom
- Super Shine Hot Wax
- Kestrel Coat - total surface sealant
- Wheel Bright
- Brisk & Bloom - $15
- Includes Super Glimmo
- Clear Coat Protectant
- Tire Gloss
- Super Glimmo - $11
- Includes Express Wash
- Triple Foam
- Wheel Cleaner
- Express Wash - $4

*Add-Ons
- Vellostra Ceramic - $5
- Kestrel Coat - $3
- Tire Gloss - $3

*FREE Vacuums with every purchase
* We care about the earth! We recycle our water

SIDE 2:
Mr Glimmo Logo on Top
Unlimited Monthly VIP Club
- Ultimate Glimmo - $55
- includes 10% off detail packages
- Brisk & Bloom - $45
-Super Glimmo - $30
-Express Wash - $20

* one wash tag per vehicle

Target Market(s)

sophisticated customers

Industry/Entity Type

car wash

Colors
0054AA
0677BA
7BADD7
CADEEF
E8F1F8
EE7325
F08F49
F5BC92
FAE3D3
FDF4ED

Requirements
Must have
• pictures/icons to relay what each package entails

```html
<!DOCTYPE html>
<html lang="en">
<head>
<meta charset="utf-8">
<title>Mr Glimmo Wash Menu</title>
<link href="https://fonts.googleapis.com/css2?family=Michroma&family=Raleway:wght@500&display=swap" rel="stylesheet">
<style>
:root{
  --navy:#1f3a62;
  --red:#c61f28;
  --red-dark:#8f1118;
  --blue:#1567b8;
  --blue-bright:#2a8fd8;
  --white:#f1f1f3;
  --text:#ffffff;
  --stage:#dcdcdc;
}
*{margin:0;padding:0;box-sizing:border-box}
html,body{width:1200px;height:1023px;overflow:hidden}
body{background:var(--stage);position:relative;font-family:'Michroma',sans-serif;color:var(--text)}
.card{position:absolute;top:127px;width:332px;height:765px;background:var(--navy);overflow:hidden}
.card--club{left:233px}
.card--menu{left:630px;width:329px}
.card__head{position:absolute;left:0;top:0;width:100%;background:var(--white);display:flex;align-items:center;justify-content:center;gap:10px}
.card--club .card__head{height:170px}
.card--menu .card__head{height:187px}
.brand{font-family:'Michroma',sans-serif;font-size:28px;color:var(--blue);letter-spacing:-0.5px}
.brand-dot{width:14px;height:14px;border-radius:50%;background:var(--red)}
.club__bar{position:absolute;left:18px;top:161px;width:297px;height:12px;border-radius:10px 10px 0 0;background:linear-gradient(90deg,var(--blue),var(--blue-bright),var(--blue))}
.club__splash{position:absolute;left:0;top:170px;width:332px;height:225px}
.club__title{position:absolute;left:29px;top:190px;font-size:23px;line-height:31px;text-transform:uppercase}
.row{position:absolute;left:0;width:100%}
.row__name{position:absolute;font-size:14px;text-transform:uppercase;white-space:nowrap;display:flex;align-items:center;transform:translateY(-50%)}
.row__dots{display:inline-block;border-bottom:1px dashed rgba(255,255,255,.8);margin-left:8px;height:0}
.price{position:absolute;width:54px;height:54px;border-radius:50%;transform:translate(-50%,-50%);display:flex;align-items:center;justify-content:center;font-size:13px;letter-spacing:-0.5px;color:#fff;white-space:nowrap}
.price--red{background:radial-gradient(circle at 62% 32%,#ffd7d7 0 8%,#e23a40 22%,var(--red) 55%,var(--red-dark) 100%)}
.price--blue{width:44px;height:44px;font-size:11px;background:radial-gradient(circle at 62% 30%,#b7dcff 0 8%,var(--blue-bright) 25%,var(--blue) 60%,#0d3f78 100%)}
.row__note{position:absolute;font-size:9.5px;line-height:16px;letter-spacing:1px;text-transform:uppercase}
.list{position:absolute;list-style:none;font-size:9.5px;line-height:16.5px;letter-spacing:1px;text-transform:uppercase}
.list li{padding-left:11px;position:relative}
.list li::before{content:"•";position:absolute;left:0}
.footnote{position:absolute;left:0;width:100%;text-align:center;font-family:'Raleway',sans-serif;font-size:12.5px;line-height:16px}
.ribbon{position:absolute;left:40px;top:170px;width:248px;height:34px;background:var(--red);clip-path:polygon(0 0,100% 0,96% 50%,100% 100%,0 100%,4% 50%);display:flex;align-items:center;justify-content:center;font-size:21px;text-transform:uppercase}
.menu__base{position:absolute;left:0;top:662px;width:100%;height:103px;background:linear-gradient(90deg,#b51820,#d42a2f,#b51820)}
.addons{position:absolute;left:25px;top:632px;width:277px;height:81px;border-radius:10px;overflow:hidden}
.addons__title{height:30px;background:var(--red);display:flex;align-items:center;justify-content:center;font-size:17px;text-transform:uppercase}
.addons__body{height:51px;background:linear-gradient(90deg,#0c4f9e,var(--blue-bright),#0c4f9e);text-align:center;font-size:8px;line-height:16px;letter-spacing:0.5px;text-transform:uppercase;padding-top:9px;white-space:nowrap}
</style>
</head>
<body>

<section class="card card--club">
  <header class="card__head">
    <span class="brand-dot"></span><span class="brand">Mr Glimmo</span>
  </header>
  <div class="club__bar"></div>
  <svg class="club__splash" viewBox="0 0 332 225" role="img" aria-label="Red paint splash with glossy droplets">
    <defs>
      <linearGradient id="splashFill" x1="0" y1="0" x2="0" y2="1">
        <stop offset="0" stop-color="#c61f28"/>
        <stop offset="1" stop-color="#9a141b"/>
      </linearGradient>
    </defs>
    <path d="M0 0H332V100C300 130 270 150 245 175C225 195 190 222 150 222C120 222 100 205 70 195C40 185 15 180 0 178Z" fill="url(#splashFill)"/>
  </svg>
  <h1 class="club__title">Unlimited<br>Monthly VIP<br>Club</h1>

  <div class="row" style="top:431px">
    <div class="row__name" style="left:27px">Ultimate Glimmo<span class="row__dots" style="width:18px"></span></div>
    <div class="price price--red" style="left:278px">$55</div>
    <p class="row__note" style="left:27px;top:24px">Includes<br>10% off detail packages</p>
  </div>
  <div class="row" style="top:525px">
    <div class="row__name" style="left:28px">Brisk &amp; Bloom<span class="row__dots" style="width:40px"></span></div>
    <div class="price price--red" style="left:278px">$45</div>
    <p class="row__note" style="left:27px;top:23px">Includes<br>10% off detail packages</p>
  </div>
  <div class="row" style="top:622px">
    <div class="row__name" style="left:28px">Super Glimmo<span class="row__dots" style="width:40px"></span></div>
    <div class="price price--red" style="left:278px">$30</div>
  </div>
  <div class="row" style="top:693px">
    <div class="row__name" style="left:30px">Express Wash<span class="row__dots" style="width:30px"></span></div>
    <div class="price price--red" style="left:278px">$20</div>
  </div>
  <p class="footnote" style="top:736px">* One Wash Tag Per Vehicle</p>
</section>

<section class="card card--menu">
  <header class="card__head">
    <span class="brand-dot"></span><span class="brand">Mr Glimmo</span>
  </header>
  <div class="ribbon">Wash Menu</div>

  <div class="row" style="top:248px">
    <div class="row__name" style="left:28px">Ultimate Glimmo<span class="row__dots" style="width:20px"></span></div>
    <div class="price price--blue" style="left:277px">$19</div>
  </div>
  <ul class="list" style="left:28px;top:271px">
    <li>Includes Brisk &amp; Bloom</li>
    <li>Super Shine Hot Wax</li>
    <li>Kestrel Coat -<br>Total Surface Sealant</li>
    <li>Wheel Bright</li>
  </ul>

  <div class="row" style="top:383px">
    <div class="row__name" style="left:28px">Brisk &amp; Bloom<span class="row__dots" style="width:40px"></span></div>
    <div class="price price--blue" style="left:277px">$15</div>
  </div>
  <ul class="list" style="left:28px;top:404px">
    <li>Includes Super Glimmo</li>
    <li>Clear Coat Protectant</li>
    <li>Tire Gloss</li>
  </ul>

  <div class="row" style="top:485px">
    <div class="row__name" style="left:28px">Super Glimmo<span class="row__dots" style="width:45px"></span></div>
    <div class="price price--blue" style="left:277px">$11</div>
  </div>
  <ul class="list" style="left:28px;top:508px">
    <li>Includes Express Wash</li>
    <li>Triple Foam</li>
    <li>Wheel Cleaner</li>
  </ul>

  <div class="row" style="top:595px">
    <div class="row__name" style="left:28px">Express Wash<span class="row__dots" style="width:36px"></span></div>
    <div class="price price--blue" style="left:277px">$4</div>
  </div>

  <div class="menu__base"></div>
  <div class="addons">
    <div class="addons__title">Add-Ons</div>
    <div class="addons__body">Vellostra Ceramic - $5<br>Kestrel Coat - $3 &nbsp;|&nbsp; Tire Gloss - $3</div>
  </div>
  <p class="footnote" style="top:721px">*FREE Vacuums with every purchase<br>* We care about the earth! We recycle our water</p>
</section>

</body>
</html>
```